Qorta Labs

I am a CBD Manufacturer I would have a site more laid out in a lab format
current site is qortalabs-example.com what Id like is a site like brimwoodlabs-example.com

Target Market(s)

Any one needing cbd oil and finished goods

Coding

Coded - Design and coding required

Number of Pages Required

1 page

```html
<!DOCTYPE html>
<html lang="en">
<head>
<meta charset="utf-8">
<title>Qorta Labs – Shop</title>
<link rel="stylesheet" href="https://fonts.googleapis.com/css2?family=Montserrat:wght@400;500;600;700&family=Open+Sans:wght@400;600&display=swap">
<style>
  :root {
    --teal: #1f7486;
    --teal-dark: #1b5c6c;
    --band: #d9d9d9;
    --footer-bg: #ececec;
    --ink: #1a1a1a;
    --muted: #555;
    --rule: #b8b8b8;
    --white: #ffffff;
  }
  * { margin: 0; padding: 0; box-sizing: border-box; }
  html, body { width: 1200px; height: 1200px; overflow: hidden; background: var(--white); }
  body { position: relative; font-family: "Montserrat", sans-serif; color: var(--ink); }

  .site-header {
    position: absolute; left: 247px; top: 0; width: 683px; height: 37px;
    background: var(--band);
  }
  .brand {
    position: absolute; display: flex; align-items: center; gap: 5px;
    font-family: "Montserrat", sans-serif; font-weight: 700; color: var(--teal);
    text-transform: uppercase; letter-spacing: 0.5px;
  }
  .brand-mark { width: 14px; height: 14px; background: var(--teal); }
  .site-header .brand { left: 64px; top: 11px; font-size: 13px; }
  .main-nav {
    position: absolute; left: 401px; top: 13px; display: flex; align-items: center;
    font-family: "Open Sans", sans-serif; font-size: 9px; color: var(--ink);
  }
  .main-nav a { color: inherit; text-decoration: none; margin-right: 13px; }
  .cart-icon { position: absolute; left: 587px; top: 8px; }

  .section-title {
    position: absolute; font-size: 13px; font-weight: 600; color: var(--teal-dark);
    transform: translateX(-50%); white-space: nowrap;
  }

  .product-photo { position: absolute; border-radius: 6px; }
  .product-name {
    position: absolute; transform: translateX(-50%); white-space: nowrap;
    font-family: "Open Sans", sans-serif; font-size: 9px; letter-spacing: 1px; color: var(--ink);
  }
  .add-to-cart {
    position: absolute; width: 110px; height: 22px; border-radius: 11px;
    background: var(--teal); color: var(--white); border: none;
    font-family: "Montserrat", sans-serif; font-size: 7px; font-weight: 700; letter-spacing: 0.8px;
    box-shadow: 0 3px 5px rgba(0,0,0,0.22);
  }

  .site-footer {
    position: absolute; left: 247px; top: 1003px; width: 683px; height: 173px;
    background: var(--footer-bg); font-size: 7.5px;
  }
  .site-footer .brand { left: 64px; top: 30px; font-size: 13px; }
  .contact-block { position: absolute; left: 64px; top: 59px; line-height: 13.5px; color: var(--muted); }
  .contact-block .email { color: var(--teal); }
  .contact-block .hours { color: var(--ink); line-height: 9px; margin-top: 2px; }
  .footer-col { position: absolute; top: 42px; }
  .footer-col h3 { font-size: 8px; font-weight: 600; color: var(--teal); letter-spacing: 0.4px; margin-bottom: 5px; }
  .footer-col p { color: var(--muted); line-height: 10.5px; width: 180px; }
  .footer-col ul { list-style: none; color: var(--muted); line-height: 13.2px; }
  .disclaimer { left: 194px; }
  .quick-links { left: 417px; }
  .follow-us { left: 562px; }
  .footer-rule { position: absolute; left: 64px; top: 138px; width: 557px; border-top: 1px solid var(--rule); }
  .copyright { position: absolute; left: 0; width: 683px; top: 152px; text-align: center; font-size: 6.5px; color: var(--teal); }
</style>
</head>
<body>

<header class="site-header">
  <div class="brand"><span class="brand-mark"></span>Qorta Labs</div>
  <nav class="main-nav">
    <a href="#">HOME</a><a href="#">ABOUT US</a><a href="#">SHOP</a><a href="#">CONTACT</a>
  </nav>
  <svg class="cart-icon" width="18" height="18" viewBox="0 0 18 18" aria-label="Cart">
    <path d="M1 4h2.5l2 8h8l1.6-6H5" fill="none" stroke="#333" stroke-width="1.1" stroke-linejoin="round"/>
    <circle cx="6.5" cy="14.5" r="1.1" fill="#333"/>
    <circle cx="12.5" cy="14.5" r="1.1" fill="#333"/>
    <circle cx="15" cy="4" r="3" fill="var(--teal)"/>
  </svg>
</header>

<main>
  <h2 class="section-title" style="left:588px; top:59px;">Topicals</h2>

  <div class="product-photo" role="img" aria-label="Group of purple CBD tincture dropper bottles" style="left:385px; top:110px; width:180px; height:148px; background:linear-gradient(180deg,#4a4690,#2a2660);"></div>
  <span class="product-name" style="left:475px; top:264px;">Tincture</span>
  <button class="add-to-cart" style="left:420px; top:289px;">ADD TO CART</button>

  <div class="product-photo" role="img" aria-label="Black squeeze tube of CBD lotion" style="left:688px; top:108px; width:62px; height:146px; background:linear-gradient(180deg,#2a2a2a,#111);"></div>
  <span class="product-name" style="left:718px; top:264px;">Lotion</span>
  <button class="add-to-cart" style="left:663px; top:289px;">ADD TO CART</button>

  <div class="product-photo" role="img" aria-label="Round metal tin of CBD salve" style="left:408px; top:370px; width:132px; height:130px; border-radius:50%; background:radial-gradient(circle,#9aa7a8,#5f6668);"></div>
  <span class="product-name" style="left:474px; top:510px;">Salve</span>
  <button class="add-to-cart" style="left:419px; top:535px;">ADD TO CART</button>

  <div class="product-photo" role="img" aria-label="Slim blue roll-on ointment bottle" style="left:702px; top:352px; width:34px; height:150px; background:linear-gradient(180deg,#2b1c14,#23207a 30%,#1c1a60);"></div>
  <span class="product-name" style="left:718px; top:510px;">Roll-on Ointment</span>
  <button class="add-to-cart" style="left:663px; top:535px;">ADD TO CART</button>

  <h2 class="section-title" style="left:483px; top:593px;">Edibles</h2>
  <h2 class="section-title" style="left:726px; top:593px;">Vape Cartridges</h2>

  <div class="product-photo" role="img" aria-label="Stacked jars of CBD gummies" style="left:380px; top:643px; width:216px; height:247px; background:linear-gradient(180deg,#1e2530,#5a3a2a 60%,#2a2a2a);"></div>
  <span class="product-name" style="left:484px; top:897px;">Gummies</span>
  <button class="add-to-cart" style="left:429px; top:922px;">ADD TO CART</button>

  <div class="product-photo" role="img" aria-label="Vape cartridge in clear blister pack" style="left:659px; top:650px; width:144px; height:232px; background:linear-gradient(180deg,#efefef,#d6d6d6);"></div>
  <span class="product-name" style="left:731px; top:891px;">Vape Pen</span>
  <button class="add-to-cart" style="left:676px; top:917px;">ADD TO CART</button>
</main>

<footer class="site-footer">
  <div class="brand"><span class="brand-mark"></span>Qorta Labs</div>
  <address class="contact-block" style="font-style:normal;">
    48 Orchard Row<br>
    Fenmore, CA 90017<br>
    1-800-555-0142<br>
    <span class="email">info@qortalabs-example.com</span>
    <div class="hours">Monday - Friday<br>8:00 AM - 5:00 PM CT</div>
  </address>
  <div class="footer-col disclaimer">
    <h3>DISCLAIMER</h3>
    <p>The statements regarding these products have not been evaluated by the Food and Drug Administration. These products are not intended to diagnose, treat, cure or prevent any disease. Results from products may vary.</p>
  </div>
  <div class="footer-col quick-links">
    <h3>QUICK LINKS</h3>
    <ul><li>Mission</li><li>Customer Satisfaction</li><li>Shipping &amp; Return Policy</li><li>Privacy Policy</li><li>Terms of Service</li></ul>
  </div>
  <div class="footer-col follow-us">
    <h3>FOLLOW US</h3>
    <ul><li>Friendloop</li><li>Chirpline</li><li>Snapgrid</li></ul>
  </div>
  <div class="footer-rule"></div>
  <p class="copyright">© 2020 Qorta Labs. All Rights Reserved.</p>
</footer>

</body>
</html>
```